Wordpress Design Project

i bought a wordpress template, bought my domain and my hosting package. i need someone to pull it all together and design my website and get it up and running.

i have the content, the logos, the look and feel of my design and i will provide these to you. I will need the headings on the theme to change and there will need to be some customization, including the the Social Icons-would need new icons creating similar in look to the existing ones, and then some minor code changes to have a new option appear in the Theme Options panel (ie; Enter your Linkedin username: , rss feed)

i will want one of the pull down tabs to have

I will want the wordpress theme to be SEO optimized. The site is optimized with SEO in mind, but also want the free WordPress plugin called Rankwise Suite added and any others that you feel are compelling.

the theme is: http://layoutbazaar.example/item/prism-adaptive-clean-html5-theme/4827365?WT.ac=category_item&WT.seg_1=category_item&WT.z_author=DovikStellan

The following design brief gives more information:

- Business Name? Bright Harbor Collective, LLC dba Bright Harbor Collective

- What do you do? Build coalitions for social good

- How many pages do you need designed and code? see template

- What is your industry? social entrepreneurship

- Describe the target audience for your website design? general public

- What 3 things would you like to communicate to your audience through your website design? 1. we are progressive 2. We use the power and merits of Capitalism to transcend poverty, preserve our planet and harness the collective power of the people 3. we are change makers
- How is your company different from your competitors? i invented a business model that will accomplish the above.

- What website design styles do you like? see theme
- What colors do you want to see in your website design? see theme and see my logo/business card.
- What colors do you NOT want to see in your website design? want to stay consistent with current design.
- What adjectives should best describe your website design? modern, artsy, engaging
- What content must be included in the website design? i will provide that later

ill also want you to provide what a process for working with me, including timeline.

the headers will be 

Home
Who We Are
What We Do
Our Projects
Blog
Latest News
Contact Us

What I am looking for is a mock up of the home page to mimic the prism wordpress theme.  the first project we will be working on is bringing vertical urban farming/manufactured in buildings - in disadvantaged neighborhoods. 

i have uploaded an executive summary so you know what we do as a company.

I would like to see what images you come up with and how you will incorporate the logo / existing look and feel into the home page.  this will give me a good idea of whom I would like to hire for the job.  this way you are not spending too much time and I can spot what i like immediately.

please also include your capacity to code according to what is required in the prism theme.  i want to make sure you are not just a graphic designer as I need the backend and some coding capacity.

thanks.

Target Market(s)

general public / corporate america

Industry/Entity Type

Progressive

Requirements
Must have
• even though this is a corporate website, i want the site to be artsy. i like the grey/black and white look and feel of what the template looks like and i want orange as the highlight color.

i will be adding color photos and video to the site. which i do not have yet.

i uploaded the logo and watermark, along with the front and back of my business card so that we remain consistent.

the watermark is used on my stationary and email template.

i will also need the control panel turned over to me when finished so that i may manage going forward.

i would also like to have an ongoing relationship with the web designer as I will be creating other sites as my business takes off.

```html
<!DOCTYPE html>
<html lang="en">
<head>
<meta charset="utf-8">
<title>Bright Harbor Collective — Core Values &amp; Latest Projects</title>
<link rel="stylesheet" href="https://fonts.googleapis.com/css2?family=Roboto+Condensed:wght@700&family=Arimo:ital,wght@0,400;0,700;1,400;1,700&display=swap">
<style>
  :root {
    --page-bg: #ffffff;
    --ink-dark: #222222;
    --ink-body: #7a7a7a;
    --accent: #ef5a1c;
    --rule: #c9c9c9;
    --frame: #e2e2e2;
    --bar: #cccccc;
  }
  * { margin: 0; padding: 0; box-sizing: border-box; }
  html, body {
    width: 1093px;
    height: 1200px;
    overflow: hidden;
    background: var(--page-bg);
    font-family: "Arimo", Arial, sans-serif;
  }
  .page { position: relative; width: 1093px; height: 1200px; }

  .section-head {
    position: absolute;
    left: 0;
    width: 1093px;
    display: flex;
    align-items: center;
  }
  .section-head__title {
    position: absolute;
    font-family: "Roboto Condensed", "Arial Narrow", sans-serif;
    font-weight: 700;
    font-size: 23px;
    letter-spacing: 0.3px;
    color: var(--ink-dark);
    text-transform: uppercase;
    white-space: nowrap;
  }
  .section-head__divider {
    position: absolute;
    left: 245px;
    width: 2px;
    background: var(--rule);
  }
  .section-head__tagline {
    position: absolute;
    left: 275px;
    font-style: italic;
    font-size: 17px;
    color: var(--accent);
    white-space: nowrap;
  }

  .core-values-head { top: 46px; height: 68px; }
  .core-values-head .section-head__title { left: 74px; }
  .core-values-head .section-head__divider { top: 0; height: 68px; }
  .core-values-head .section-head__tagline { left: 275px; width: 805px; }

  .projects-head { top: 494px; height: 67px; }
  .projects-head .section-head__title { left: 31px; }
  .projects-head .section-head__divider { top: 0; height: 67px; }

  .values-list { position: absolute; left: 0; top: 0; }
  .value-row {
    position: absolute;
    left: 0;
    width: 1000px;
    display: flex;
  }
  .value-row__label {
    width: 188px;
    text-align: right;
    font-weight: 700;
    font-style: italic;
    font-size: 13.5px;
    color: var(--accent);
    white-space: nowrap;
    padding-top: 1px;
  }
  .value-row__text {
    margin-left: 15px;
    width: 770px;
    font-size: 12.4px;
    line-height: 16px;
    color: var(--ink-body);
  }

  .project-grid {
    position: absolute;
    left: 41px;
    top: 622px;
    display: grid;
    grid-template-columns: repeat(3, 306px);
    grid-template-rows: 289px 256px;
    column-gap: 54px;
  }
  .project-card__frame {
    width: 306px;
    height: 185px;
    border: 3px solid var(--frame);
    padding: 3px;
  }
  .project-card__photo { width: 100%; height: 100%; }
  .project-card__title {
    margin-top: 16px;
    font-family: "Roboto Condensed", "Arial Narrow", sans-serif;
    font-weight: 700;
    font-size: 15.5px;
    color: var(--ink-dark);
    text-transform: uppercase;
    line-height: 18px;
  }
  .project-card__subtitle {
    font-size: 13px;
    color: var(--accent);
    line-height: 17px;
  }
  .project-card__bar {
    margin-top: 22px;
    width: 306px;
    height: 7px;
    background: var(--bar);
  }

  .photo--chart { background: linear-gradient(160deg, #f4e7cf, #e9d6b4); }
  .photo--climb { background: linear-gradient(160deg, #ececec, #bdbdbd); }
  .photo--seedling { background: linear-gradient(160deg, #4a4a4a, #262626); }
  .photo--pie { background: linear-gradient(160deg, #f6ecd6, #e4cfa9); }
  .photo--signs { background: linear-gradient(160deg, #8e9aa6, #3b4652); }
  .photo--bull { background: linear-gradient(160deg, #9aa19c, #3a3530); }
</style>
</head>
<body>
<main class="page">

  <header class="section-head core-values-head">
    <h2 class="section-head__title">Core Values</h2>
    <span class="section-head__divider"></span>
    <p class="section-head__tagline">We continue to deepen, embrace and allow eight core values to more effectively guide us in our actions:</p>
  </header>

  <section class="values-list">
    <div class="value-row" style="top:174px">
      <span class="value-row__label">Social Contribution:</span>
      <p class="value-row__text">We are driven by our sense of duty, integrity and moral conscience. We understand that the primary purpose of money is to serve and enrich humanity.</p>
    </div>
    <div class="value-row" style="top:220px">
      <span class="value-row__label">Entrepreneurial Spirit:</span>
      <p class="value-row__text">We engage the power of possibility with a bias for inspired action. In the absence of a clear solution, we create one.</p>
    </div>
    <div class="value-row" style="top:252px">
      <span class="value-row__label">Breakthrough Execution:</span>
      <p class="value-row__text">We are anchored in purpose, aligned in action and relentless in achieving our goals. Where there is a will, there is a way.</p>
    </div>
    <div class="value-row" style="top:285px">
      <span class="value-row__label">Open-Minded Optimism:</span>
      <p class="value-row__text">We are disciplined, dedicated and forthright. We are unlimited in our power and possibility and dedicated to our mission.</p>
    </div>
    <div class="value-row" style="top:318px">
      <span class="value-row__label">Mutual Respect:</span>
      <p class="value-row__text">We respect ourselves, our colleagues, the community and the planet. We continue to work on effectively listening to, accepting and understanding the "perfection of our imperfections."</p>
    </div>
    <div class="value-row" style="top:364px">
      <span class="value-row__label">100% Responsibility:</span>
      <p class="value-row__text">We strive for excellence and are 100% accountable for our continued growth.</p>
    </div>
    <div class="value-row" style="top:397px">
      <span class="value-row__label">Generous Spirit:</span>
      <p class="value-row__text">We know that our success is dependent on the success of those around us. We work together to align our gifts/talents/needs/desires to best serve our company, clients and community.</p>
    </div>
  </section>

  <header class="section-head projects-head">
    <h2 class="section-head__title">Latest Projects</h2>
    <span class="section-head__divider"></span>
    <p class="section-head__tagline">See what we have done....</p>
  </header>

  <section class="project-grid">
    <article class="project-card">
      <div class="project-card__frame"><div class="project-card__photo photo--chart" role="img" aria-label="Hand pointing at a rising multicolour line chart"></div></div>
      <h3 class="project-card__title">Lorel ipsum dolor sit amet</h3>
      <p class="project-card__subtitle">Lorel ipsum dolor sit amet</p>
    </article>
    <article class="project-card">
      <div class="project-card__frame"><div class="project-card__photo photo--climb" role="img" aria-label="Two businessmen pulling a rope up a rising line"></div></div>
      <h3 class="project-card__title">Lorel ipsum dolor sit amet</h3>
      <p class="project-card__subtitle">Lorel ipsum dolor sit amet</p>
    </article>
    <article class="project-card">
      <div class="project-card__frame"><div class="project-card__photo photo--seedling" role="img" aria-label="Cupped hands holding soil with a green seedling"></div></div>
      <h3 class="project-card__title">Lorel ipsum dolor sit amet</h3>
      <p class="project-card__subtitle">Lorel ipsum dolor sit amet</p>
    </article>
    <article class="project-card">
      <div class="project-card__frame"><div class="project-card__photo photo--pie" role="img" aria-label="Hands pulling slices from a red paper pie chart"></div></div>
      <h3 class="project-card__title">Lorel ipsum dolor sit amet</h3>
      <p class="project-card__subtitle">Lorel ipsum dolor sit amet</p>
      <div class="project-card__bar"></div>
    </article>
    <article class="project-card">
      <div class="project-card__frame"><div class="project-card__photo photo--signs" role="img" aria-label="Street signs at a downtown financial district corner"></div></div>
      <h3 class="project-card__title">Lorel ipsum dolor sit amet</h3>
      <p class="project-card__subtitle">Lorel ipsum dolor sit amet</p>
      <div class="project-card__bar"></div>
    </article>
    <article class="project-card">
      <div class="project-card__frame"><div class="project-card__photo photo--bull" role="img" aria-label="Bronze bull statue on a city plaza"></div></div>
      <h3 class="project-card__title">Lorel ipsum dolor sit amet</h3>
      <p class="project-card__subtitle">Lorel ipsum dolor sit amet</p>
      <div class="project-card__bar"></div>
    </article>
  </section>

</main>
</body>
</html>
```